【 概要 】 当社では、M&A業界に転職を考える求職者向けの転職支援サービスの立ち上げを行っています。 サイト名は「M&A WORK HARBOR」と言い、当社が運営する法律専門職向け転職サイト「LEGAL WORK HARBOR」の姉妹サイトです。 https://legal-work-harbor-example.com/ そのサービス(M&A WORK HARBOR)のLPのファーストビュー部分のデザインを依頼したいと思います。 【コンペ内容】 ワイヤーフレーム(PC)のファーストビュー付近に赤でラインを引いています。 そこまでのデザインでコンペをさせていただきます。 【 依頼内容 】 ・依頼工程:デザインのみ ・作業ボリューム:PC・スマホ1P(コンペはファーストビューのみ) 【 提供素材 】 ・ワイヤー、ラフ案:PCのみあり (添付PDF参照) ・画像:あり (添付画像参照、我々のイメージに近い写真を選定していますが、より良いイメージがあればご提案いただいても構いません。) 【 デザインイメージ 】 ・ターゲットペルソナ:29歳金融業界(大手メガバンク、証券会社)の男性。 ・雰囲気:シンプルでスタイリッシュ、モダンかつ高級感のあるデザイン。 ・参考サイト:https://kvemu-example.co.jp/lp/ 【ロゴについて】 添付します 【その他デザイン参考ページ】 https://legal-work-harbor-example.com/lawyer/lp/steps/ ↑当社の別サービスのデザインです 【 納期 】 2024年2月14日 ※コンペ以外のデザイン部分に関しては、コンペ終了後1〜2週間程度を想定しています。 【 報酬 】 12万円 【 追加依頼 】 HTMLコーディングの追加発注も検討しています。 総額20万くらいでHTMLまで完成させたいと考えていますので、追加8万ほどで発注できればと考えております。 ご検討よろしくお願いします。 HTMLに自信がなければ、その部分のみ他の方に発注も可能です。 ご質問がありましたら、気軽にお問い合わせください。 応募をお待ちしております! |
採用の理由
・修正案のイメージが非常に良かったこと
・コーディングまでの依頼が一気通貫でできること
・ポートフォリオからデザイン力が保証できることが理解できたこと
から採用させていただきます。
引き続きよろしくお願いします!
応募者全員へのお礼・コメント
みなさまからの多くのご提案大変ありがとうございました。
今回採用させていただいた理由として
・こちらの意図をよく理解してデザインに反映してくれたこと(修正案もいただきましたが、さらにクオリティが上がっていました)
ことなどを理由に採用させていただきました。
またご機会がありましたら、何卒よろしくお願いいたします。

```html
<!DOCTYPE html>
<html lang="ja">
<head>
<meta charset="utf-8">
<title>M&amp;A WORK HARBOR</title>
<link href="https://fonts.googleapis.com/css2?family=Noto+Sans+JP:wght@400;500;700&display=swap" rel="stylesheet">
<style>
  :root{
    --navy:#1d2b48;
    --navy-deep:#15203a;
    --gold:#b8955a;
    --gold-light:#cfb283;
    --white:#ffffff;
    --ink:#333a46;
    --muted:#6b7280;
    --field:#e9ecf1;
    --section:#f2f2f2;
  }
  *{box-sizing:border-box;margin:0;padding:0}
  html,body{width:1128px;height:1200px;overflow:hidden}
  body{font-family:"Noto Sans JP",sans-serif;color:var(--ink);background:var(--section);position:relative}

  .hero{position:absolute;left:0;top:0;width:1128px;height:547px;overflow:hidden}
  .hero-photo{position:absolute;inset:0;
    background:
      radial-gradient(ellipse 260px 330px at 560px 330px, rgba(38,44,62,.85), rgba(38,44,62,0) 70%),
      linear-gradient(100deg,#4d6788 0%,#7d95b2 38%,#a9bacd 60%,#7f93ad 100%);}
  .hero-shade{position:absolute;inset:0;background:linear-gradient(90deg,rgba(28,42,70,.55) 0%,rgba(28,42,70,.15) 55%,rgba(28,42,70,0) 100%)}
  .brand{position:absolute;left:32px;top:34px;display:flex;align-items:center;gap:22px;color:var(--white)}
  .brand-name{font-weight:700;font-size:22px;letter-spacing:.02em}
  .brand-tag{font-size:12px;font-weight:500;opacity:.9}
  .headline{position:absolute;left:32px;top:200px;color:var(--white);font-weight:700;font-size:42px;line-height:1.45;letter-spacing:.04em}
  .lead{position:absolute;left:32px;top:352px;color:var(--white);font-size:15px;line-height:1.9;opacity:.92}

  .form-panel{position:absolute;left:733px;top:45px;width:328px;height:457px;background:rgba(25,37,64,.94);color:var(--white);padding:20px 24px}
  .badge{position:absolute;left:18px;top:0;width:56px;height:56px;border-radius:50%;background:var(--gold);display:flex;flex-direction:column;align-items:center;justify-content:center;font-weight:700;line-height:1.1}
  .badge small{font-size:9px}
  .badge b{font-size:16px}
  .form-title{text-align:center;font-weight:700;font-size:17px;line-height:1.35;padding-left:40px;margin-top:4px}
  .steps{position:relative;margin:20px 6px 0;height:30px}
  .steps-line{position:absolute;left:20px;right:20px;top:4px;height:1px;background:rgba(255,255,255,.55)}
  .step{position:absolute;top:0;width:9px;height:9px;border-radius:50%;background:rgba(255,255,255,.6)}
  .step.is-current{background:var(--gold)}
  .step-label{position:absolute;top:14px;font-size:9px;white-space:nowrap;transform:translateX(-50%);opacity:.85}
  .field{margin-top:8px}
  .field-label{font-size:11px;font-weight:500}
  .field-label em{font-style:normal;font-size:9px;opacity:.8;margin-left:2px}
  .field-input{margin-top:4px;height:32px;background:var(--field);border-radius:2px;font-size:11px;color:#9aa1ad;padding:0 10px;display:flex;align-items:center}
  .birth{display:flex;align-items:center;gap:6px;margin-top:6px;font-size:11px}
  .select{height:32px;background:var(--field);border-radius:2px;position:relative}
  .select::after{content:"";position:absolute;right:8px;top:13px;border:4px solid transparent;border-top:5px solid #555}
  .next-btn{display:flex;align-items:center;justify-content:center;gap:14px;margin:32px auto 0;width:150px;height:36px;border:1px solid var(--white);font-size:13px;font-weight:500}

  .hero-rule{position:absolute;left:0;top:547px;width:1128px;height:3px;background:var(--gold)}

  .reasons-heading{position:absolute;left:368px;top:632px;width:392px;height:90px;text-align:center}
  .reasons-heading p{font-weight:700;font-size:19px;color:var(--navy);margin-top:10px;letter-spacing:.03em}
  .reasons-heading h2{font-size:25px;color:var(--gold);margin-top:2px;letter-spacing:.1em}
  .bracket{position:absolute;top:0;width:12px;height:90px;border:1px solid #7a7f88}
  .bracket.left{left:0;border-right:none}
  .bracket.right{right:0;border-left:none}

  .card{position:absolute;top:779px;width:275px;height:328px;background:var(--white);text-align:center;padding:50px 26px 0}
  .card svg{display:block;margin:0 auto}
  .card h3{margin-top:20px;color:var(--gold);font-size:18px;line-height:1.4;font-weight:700}
  .card p{margin-top:14px;font-size:12px;line-height:1.8;text-align:left;color:var(--muted)}
</style>
</head>
<body>
  <section class="hero">
    <div class="hero-photo" role="img" aria-label="スーツ姿のビジネスパーソンとオフィス街の背景写真"></div>
    <div class="hero-shade"></div>
    <div class="brand">
      <span class="brand-name">M&amp;A WORK HARBOR</span>
      <span class="brand-tag">M&amp;A業界の転職に、最適なパートナーを。</span>
    </div>
    <h1 class="headline">M&amp;A業界への転職には、<br>パートナーが必要だ。</h1>
    <p class="lead">M&amp;A WORK HARBORは、M&amp;A業界を経験した専門の<br>キャリアアドバイザーによる転職支援サービスです。</p>

    <form class="form-panel">
      <div class="badge"><small>登録</small><b>60秒</b></div>
      <div class="form-title">M&amp;A専門アドバイザーに<br>相談する</div>
      <div class="steps">
        <div class="steps-line"></div>
        <span class="step is-current" style="left:16px"></span>
        <span class="step" style="left:136px"></span>
        <span class="step" style="left:256px"></span>
        <span class="step-label" style="left:20px">プロフィール</span>
        <span class="step-label" style="left:140px">希望条件</span>
        <span class="step-label" style="left:260px">登録完了</span>
      </div>
      <div class="field"><div class="field-label">お名前<em>(必須)</em></div><div class="field-input">例:佐藤 一郎</div></div>
      <div class="field"><div class="field-label">メールアドレス<em>(必須)</em></div><div class="field-input">例:sample@example.com</div></div>
      <div class="field"><div class="field-label">電話番号<em>(必須)</em></div><div class="field-input">例:09012345678</div></div>
      <div class="field">
        <div class="field-label">生年月日<em>(必須)</em></div>
        <div class="birth">
          <div class="select" style="width:100px"></div><span>年</span>
          <div class="select" style="width:60px"></div><span>月</span>
          <div class="select" style="width:60px"></div><span>日</span>
        </div>
      </div>
      <div class="next-btn">次へ
        <svg width="22" height="8" viewBox="0 0 22 8"><path d="M0 7H20L14 1" fill="none" stroke="#fff" stroke-width="1.2"/></svg>
      </div>
    </form>
  </section>
  <div class="hero-rule"></div>

  <div class="reasons-heading">
    <span class="bracket left"></span><span class="bracket right"></span>
    <p>M&amp;A WORK HARBORが選ばれる</p>
    <h2>理由</h2>
  </div>

  <article class="card" style="left:120px">
    <svg width="80" height="80" viewBox="0 0 80 80" fill="none" stroke="#1d2b48" stroke-width="2.5">
      <circle cx="26" cy="20" r="8"/>
      <path d="M12 62V42c0-7 6-12 14-12s14 5 14 12v20"/>
      <path d="M26 32l-3 6 3 14 3-14z"/>
      <circle cx="56" cy="44" r="13"/><circle cx="56" cy="44" r="7"/>
      <circle cx="56" cy="44" r="2" fill="#b8955a" stroke="none"/>
      <path d="M56 44l14-14M66 28h5v5" stroke="#b8955a"/>
    </svg>
    <h3>エージェント自身が<br>M&amp;Aのプロ</h3>
    <p>エージェント自身がM&amp;A業界を経験しているため、紹介企業の特性を理解し、最適な企業の提案が可能。</p>
  </article>

  <article class="card" style="left:427px">
    <svg width="80" height="80" viewBox="0 0 80 80" fill="none" stroke="#1d2b48" stroke-width="2.5">
      <rect x="14" y="10" width="38" height="54" rx="2"/>
      <path d="M20 22l3 3 5-6M20 34l3 3 5-6M20 46l3 3 5-6"/>
      <path d="M33 23h12M33 35h8"/>
      <circle cx="54" cy="52" r="11" stroke="#b8955a"/>
      <path d="M62 60l10 10" stroke="#b8955a" stroke-width="3"/>
    </svg>
    <h3>まずは情報収集に<br>最適</h3>
    <p>気軽にセッティングできるオンラインカウンセリングで、業界知識を深める。</p>
  </article>

  <article class="card" style="left:733px">
    <svg width="80" height="80" viewBox="0 0 80 80" fill="none" stroke="#1d2b48" stroke-width="2.5">
      <path d="M56 8v26"/>
      <path d="M56 9l14 5-14 5" fill="#1d2b48"/>
      <path d="M56 34H30a8 8 0 0 0 0 16h22a8 8 0 0 1 0 16H16"/>
      <circle cx="14" cy="66" r="3" fill="#b8955a" stroke="none"/>
    </svg>
    <h3>大手M&amp;A企業と<br>繋がるパイプ</h3>
    <p>紹介先のほとんどは経営者クラスとの独自のパイプを構築済み。選考を有利に進める。</p>
  </article>
</body>
</html>
```